Harrowgate Financial Coaching LLC - Needed clean black business card

Business card for personal financial coaching practice located on Las Vegas NV, new startup. Back of card needs to have "how it works" to match the website.

Font styles to use
Sans Serif

Colors

Designer to choose colors to be used in the design.

```html
<!DOCTYPE html>
<html lang="en">
<head>
<meta charset="utf-8">
<title>Harrowgate Financial Coaching LLC – Business Card</title>
<link rel="stylesheet" href="https://fonts.googleapis.com/css2?family=Montserrat:wght@400;500;700;800&display=swap">
<style>
  :root {
    --backdrop: #e4e4e2;
    --card: #0d0d0d;
    --ink: #ffffff;
    --ink-soft: #e6e6e6;
    --rule: #cfcfcf;
  }
  * { box-sizing: border-box; margin: 0; padding: 0; }
  html, body {
    width: 1200px; height: 852px; overflow: hidden;
    background: var(--backdrop);
    font-family: "Montserrat", sans-serif;
    color: var(--ink);
  }
  .sheet {
    width: 1200px; height: 852px;
    display: flex; flex-direction: column; align-items: center; justify-content: center;
    gap: 28px;
  }
  .card {
    width: 700px; height: 400px;
    background: var(--card);
    border-radius: 26px;
    position: relative;
    box-shadow: 0 6px 18px rgba(0,0,0,.22);
  }
  .wordmark {
    text-align: center;
    font-weight: 700;
    font-size: 25px;
    letter-spacing: 1.5px;
    text-transform: uppercase;
    line-height: 1.25;
  }
  /* back */
  .card--back .wordmark { position: absolute; top: 58px; left: 0; right: 0; }
  .how-title {
    position: absolute; top: 160px; left: 0; right: 0;
    text-align: center; font-weight: 800; font-size: 19px; letter-spacing: .5px;
  }
  .how-rule { position: absolute; top: 192px; left: 210px; width: 280px; height: 8px; }
  .how-copy {
    position: absolute; top: 222px; left: 70px; right: 70px;
    text-align: center; font-size: 13.5px; font-weight: 500; line-height: 1.95;
    letter-spacing: .6px; color: var(--ink-soft);
  }
  .how-url { display: block; font-weight: 700; color: var(--ink); }
  /* front */
  .card--front .wordmark { position: absolute; top: 74px; left: 0; right: 0; }
  .person {
    position: absolute; top: 226px; left: 70px; width: 300px; text-align: right;
  }
  .person__name { font-weight: 800; font-size: 24px; letter-spacing: 1px; }
  .person__role { font-weight: 500; font-size: 15px; margin-top: 4px; letter-spacing: .5px; }
  .divider { position: absolute; top: 200px; left: 392px; width: 1px; height: 140px; background: var(--rule); }
  .contact {
    position: absolute; top: 196px; left: 412px; right: 30px;
    font-size: 13.5px; font-weight: 400; letter-spacing: .4px; line-height: 1.45;
  }
  .contact__address { margin-bottom: 12px; }
  .contact__row { display: flex; align-items: center; gap: 8px; margin-top: 4px; }
  .contact__row svg { width: 12px; height: 12px; flex: none; }
</style>
</head>
<body>
<main class="sheet">

  <section class="card card--back" aria-label="Card back">
    <div class="wordmark">Harrowgate Financial<br>Coaching LLC</div>
    <h2 class="how-title">How It Works</h2>
    <svg class="how-rule" viewBox="0 0 280 8" aria-hidden="true">
      <line x1="0" y1="4" x2="280" y2="4" stroke="#cfcfcf" stroke-width="1"/>
      <circle cx="140" cy="4" r="3" fill="#ffffff"/>
    </svg>
    <p class="how-copy">
      All free one-time consultations are in-person meetings only. Paid appointments
      may be scheduled for in-person or virtual meetings. Select the session, date and
      time that works best for your schedule. Start your journey of financial freedom at
      <span class="how-url">harrowgatecoaching.com</span>
    </p>
  </section>

  <section class="card card--front" aria-label="Card front">
    <div class="wordmark">Harrowgate Financial<br>Coaching LLC</div>
    <div class="person">
      <div class="person__name">Dana Harrowgate</div>
      <div class="person__role">Manager</div>
    </div>
    <div class="divider"></div>
    <div class="contact">
      <div class="contact__address">4120 W Sahara Ave #108-B<br>Las Vegas, NV 89102</div>
      <div class="contact__row">
        <svg viewBox="0 0 24 24" aria-hidden="true"><path fill="#fff" d="M6.6 10.8a15 15 0 0 0 6.6 6.6l2.2-2.2c.3-.3.7-.4 1-.2 1.1.4 2.3.6 3.6.6.6 0 1 .4 1 1V20c0 .6-.4 1-1 1A17 17 0 0 1 3 4c0-.6.4-1 1-1h3.5c.6 0 1 .4 1 1 0 1.3.2 2.5.6 3.6.1.3 0 .7-.2 1z"/></svg>
        <span>702-555-0184</span>
      </div>
      <div class="contact__row">
        <svg viewBox="0 0 24 24" aria-hidden="true"><rect x="2" y="5" width="20" height="14" rx="1.5" fill="#fff"/><path d="M3 6l9 7 9-7" fill="none" stroke="#0d0d0d" stroke-width="2"/></svg>
        <span>dana@harrowgatecoaching.com</span>
      </div>
      <div class="contact__row">
        <svg viewBox="0 0 24 24" aria-hidden="true"><circle cx="12" cy="12" r="10" fill="#fff"/><path d="M2 12h20M12 2c3 3 3 17 0 20M12 2c-3 3-3 17 0 20" fill="none" stroke="#0d0d0d" stroke-width="1.5"/></svg>
        <span>www.harrowgatecoaching.com</span>
      </div>
    </div>
  </section>

</main>
</body>
</html>
```